Calder Pizza - Takeout Menu Design

We are looking for a takeout menu design.
We are looking for a( 5" x 8.5" DOUBLE SIDED) flyer with our available pizza flavors
Must be easy to ready and not "busy"

Must include our logo (attached)
website: www.calderpizza.ca
address:
Fenwick Ridge Plaza
417, 318 9 Avenue SW
and the following details:
Visit our website for our complete appetizer, pasta, salad and catering menu.

Winner of this contest will also be offered to create a few print designs via printhive.

Please do not hesitate to ask any questions.

Target Market(s)

Business / Office clientele

Industry/Entity Type

Pizza place / specializing in corporate orders

Requirements
Must have
• Easy to read
Should not have
• Can not be busy or cluttered

```html
<!DOCTYPE html>
<html lang="en">
<head>
<meta charset="utf-8">
<title>Calder Pizza – Take-Out Menu</title>
<link rel="stylesheet" href="https://fonts.googleapis.com/css2?family=Raleway:wght@300;400&family=Open+Sans:wght@400;700&display=swap">
<style>
  :root {
    --paper: #fbe6e6;
    --paper-light: #fdf1f1;
    --ink: #262626;
    --red: #c8102e;
    --band: #a8141c;
    --white: #ffffff;
  }
  * { box-sizing: border-box; margin: 0; padding: 0; }
  html, body { width: 705px; height: 1200px; overflow: hidden; }
  body {
    font-family: "Open Sans", Arial, sans-serif;
    color: var(--ink);
    background: radial-gradient(ellipse at 60% 30%, var(--paper-light) 0%, var(--paper) 70%);
    position: relative;
  }
  .brand {
    position: absolute; top: 56px; left: 0; width: 705px;
    text-align: center;
    font-family: "Raleway", Arial, sans-serif;
    font-weight: 300; font-size: 72px; line-height: 84px; letter-spacing: 4px;
    color: var(--ink); text-transform: uppercase;
  }
  .address {
    position: absolute; top: 156px; left: 0; width: 705px;
    text-align: center;
    font-family: "Raleway", Arial, sans-serif;
    font-size: 25px; font-weight: 400; color: var(--ink);
  }
  .column { position: absolute; top: 228px; }
  .column--left { left: 34px; width: 312px; }
  .column--right { left: 368px; width: 322px; }
  .divider {
    position: absolute; left: 355px; top: 228px; width: 1.5px; height: 898px;
    background: var(--red);
  }
  .section-title {
    color: var(--red); font-weight: 700; font-size: 14.5px; margin-bottom: 6px;
  }
  .section-title + .classic-list { margin-bottom: 20px; }
  .classic-list li {
    list-style: none; display: grid;
    grid-template-columns: 1fr 60px 64px;
    font-size: 14px; line-height: 23.5px;
  }
  .classic-list .bullet { white-space: nowrap; }
  .price { text-align: right; white-space: nowrap; }
  .item-list { list-style: none; }
  .item { margin-bottom: 6px; font-size: 14px; line-height: 17px; }
  .column--right .item { margin-bottom: 8px; }
  .item-head {
    display: grid; grid-template-columns: 1fr 60px 64px; font-weight: 700;
  }
  .item-head .bullet { white-space: nowrap; }
  .bullet::before {
    content: "\25C6"; color: var(--red); font-size: 10px;
    display: inline-block; width: 16px; vertical-align: 2px;
  }
  .item-desc { padding-left: 16px; }
  .footnote {
    position: absolute; top: 1133px; left: 0; width: 705px;
    text-align: center; color: var(--red); font-size: 13px;
  }
  .footer-band {
    position: absolute; left: 0; bottom: 0; width: 705px; height: 40px;
    background: var(--band); color: var(--white);
    display: flex; align-items: center; justify-content: center;
    font-size: 12.5px; gap: 14px;
  }
  .footer-band .website { font-weight: 700; }
</style>
</head>
<body>
  <header>
    <div class="brand">Calder Pizza</div>
    <div class="address">Fenwick Ridge Plaza, 417, 318 9 Avenue SW</div>
  </header>

  <section class="column column--left">
    <h2 class="section-title">Classic Take-Out Pizza - 8" &amp; 13"</h2>
    <ul class="classic-list">
      <li><span class="bullet">Pepperoni &amp; Mushroom</span><span class="price">$12.99</span><span class="price">$30.95</span></li>
      <li><span class="bullet">Pepperoni</span><span class="price">$11.99</span><span class="price">$29.95</span></li>
      <li><span class="bullet">Hawaiian</span><span class="price">$12.99</span><span class="price">$30.95</span></li>
      <li><span class="bullet">Beef &amp; Mushroom</span><span class="price">$13.49</span><span class="price">$32.95</span></li>
      <li><span class="bullet">Pepperoni &amp; Ham</span><span class="price">$12.99</span><span class="price">$30.95</span></li>
      <li><span class="bullet">Ham &amp; Mushroom</span><span class="price">$12.99</span><span class="price">$30.95</span></li>
      <li><span class="bullet">Beef &amp; Onion</span><span class="price">$13.49</span><span class="price">$32.95</span></li>
      <li><span class="bullet">Cheese</span><span class="price">$11.99</span><span class="price">$29.95</span></li>
    </ul>

    <h2 class="section-title">Specialty Take-Out Pizza- 8" &amp; 13"</h2>
    <ul class="item-list">
      <li class="item"><div class="item-head"><span class="bullet">All Meat</span><span class="price">$14.99</span><span class="price">$35.95</span></div><p class="item-desc">Pepperoni, Beef &amp; Smoked Ham &amp; Bacon</p></li>
      <li class="item"><div class="item-head"><span class="bullet">Double Pepperoni</span><span class="price">$13.49</span><span class="price">$32.95</span></div><p class="item-desc">Loads of Pepperoni</p></li>
      <li class="item"><div class="item-head"><span class="bullet">Hot Honey Pepperoni</span><span class="price">$14.49</span><span class="price">$34.95</span></div><p class="item-desc">Double Pepperoni and drizzled with Hot Honey</p></li>
      <li class="item"><div class="item-head"><span class="bullet">Hawaiian Heat</span><span class="price">$13.49</span><span class="price">$32.95</span></div><p class="item-desc">Smoked Ham, Pineapple and Banana Peppers</p></li>
      <li class="item"><div class="item-head"><span class="bullet">Four Cheese</span><span class="price">$13.49</span><span class="price">$32.95</span></div><p class="item-desc">Mozzarella, Feta, Romano and Cheddar Cheese</p></li>
      <li class="item"><div class="item-head"><span class="bullet">Montreal</span><span class="price">$13.49</span><span class="price">$32.95</span></div><p class="item-desc">Pepperoni &amp; Double Smoked Bacon</p></li>
      <li class="item"><div class="item-head"><span class="bullet">Montreal Heat</span><span class="price">$13.99</span><span class="price">$33.95</span></div><p class="item-desc">Pepperoni, Double Smoked Bacon &amp; Banana Peppers</p></li>
      <li class="item"><div class="item-head"><span class="bullet">Supreme</span><span class="price">$13.49</span><span class="price">$32.95</span></div><p class="item-desc">Pepperoni, Mushrooms &amp; Green Peppers</p></li>
      <li class="item"><div class="item-head"><span class="bullet">Canadian</span><span class="price">$13.49</span><span class="price">$32.95</span></div><p class="item-desc">Pepperoni, Mushrooms &amp; Ham</p></li>
      <li class="item"><div class="item-head"><span class="bullet">BBQ Chicken</span><span class="price">$13.99</span><span class="price">$33.95</span></div><p class="item-desc">Chicken Breast, Hickory BBQ Sauce &amp; Red Onions.</p></li>
      <li class="item"><div class="item-head"><span class="bullet">BBQ Chicken Plus</span><span class="price">$14.79</span><span class="price">$34.95</span></div><p class="item-desc">Chicken Breast, Hickory BBQ Sauce, Red Onions &amp; Cilantro</p></li>
      <li class="item"><div class="item-head"><span class="bullet">Spicy BBQ Chicken</span><span class="price">$14.49</span><span class="price">$35.95</span></div><p class="item-desc">Chicken Breast, Hickory BBQ Sauce, Red Onions &amp; Banana Peppers</p></li>
    </ul>
  </section>

  <div class="divider"></div>

  <section class="column column--right">
    <ul class="item-list">
      <li class="item"><div class="item-head"><span class="bullet">Sweet Chili Chicken</span><span class="price">$14.49</span><span class="price">$35.95</span></div><p class="item-desc">Chicken Breast, Pineapple, Red Onions &amp; Sweet Chili Sauce</p></li>
      <li class="item"><div class="item-head"><span class="bullet">Chicken Club</span><span class="price">$14.79</span><span class="price">$35.95</span></div><p class="item-desc">Chicken Breast, Double Smoked Bacon, Red Onions and Tomatoes</p></li>
      <li class="item"><div class="item-head"><span class="bullet">Athenean</span><span class="price">$14.49</span><span class="price">$34.95</span></div><p class="item-desc">Chicken Breast, Spinach, Feta Cheese and Tomato</p></li>
      <li class="item"><div class="item-head"><span class="bullet">Greek Supreme</span><span class="price">$14.99</span><span class="price">$35.95</span></div><p class="item-desc">Chicken Breast, Feta Cheese, Tomato, Green Pepper, Red Onions &amp; Black Olives</p></li>
      <li class="item"><div class="item-head"><span class="bullet">Mediterranean Chkn.</span><span class="price">$14.79</span><span class="price">$35.95</span></div><p class="item-desc">Seasoned Chicken Breast, Tomatoes, Red Onions and Feta Cheese</p></li>
      <li class="item"><div class="item-head"><span class="bullet">Original Spinach</span><span class="price">$13.49</span><span class="price">$32.95</span></div><p class="item-desc">Spinach &amp; Feta Cheese</p></li>
      <li class="item"><div class="item-head"><span class="bullet">Zeus</span><span class="price">$13.95</span><span class="price">$33.95</span></div><p class="item-desc">Spinach, Feta Cheese and Tomatoes</p></li>
      <li class="item"><div class="item-head"><span class="bullet">Greek</span><span class="price">$13.99</span><span class="price">$33.95</span></div><p class="item-desc">Feta Cheese, Tomato, Green Peppers, Red Onions and Black Olives</p></li>
      <li class="item"><div class="item-head"><span class="bullet">Vegetarian</span><span class="price">$13.49</span><span class="price">$32.95</span></div><p class="item-desc">Mushrooms, Tomatoes, Green Peppers and Black Olives</p></li>
      <li class="item"><div class="item-head"><span class="bullet">Veggie Delight</span><span class="price">$13.95</span><span class="price">$33.95</span></div><p class="item-desc">Mushrooms, Tomatoes, Green Peppers, Black Olives &amp; Onions</p></li>
      <li class="item"><div class="item-head"><span class="bullet">Deluxe</span><span class="price">$14.49</span><span class="price">$34.95</span></div><p class="item-desc">Pepperoni, Mushrooms, Ham, Tomatoes, Green Peppers and Red Onions</p></li>
      <li class="item"><div class="item-head"><span class="bullet">Calder Special</span><span class="price">$14.49</span><span class="price">$34.95</span></div><p class="item-desc">Pepperoni, Mushrooms, Ham, Green Peppers and Black Olives</p></li>
      <li class="item"><div class="item-head"><span class="bullet">Dill Pickle</span><span class="price">$13.49</span><span class="price">$32.95</span></div><div class="item-head"><span></span><span class="price">$14.49</span><span class="price">$35.95</span></div><p class="item-desc">Crispy Dill Pickles, Fresh Dill with our cream based garlic sauce. Served with our without bacon.</p></li>
      <li class="item"><div class="item-head"><span class="bullet">BBQ Pulled Pork</span><span class="price">$14.49</span><span class="price">$35.95</span></div><p class="item-desc">Pulled Pork, Red Onions, Red Peppers and Cilantro.</p></li>
    </ul>
  </section>

  <p class="footnote">All of our pizzas are prepared fresh everyday using only the finest mozzarella blend and ingredients.</p>
  <footer class="footer-band">
    <span class="visit-line">Visit our website for our complete appetizer, pasta, salad and catering menu.</span>
    <span class="website">www.calderpizza.ca</span>
  </footer>
</body>
</html>
```